Stationary for Keeping Steady

we are in the process of creating a more professional image for our company Keeping Steady Paramedical Services. We have recently had a new logo and general brochure designed using artpitchhub and have been impressed by the quality of submissions.

We need:
- Letterhead (A4)
- Business Cards
- With compliments slips
- Email stationary

Letterhead information:
Address - 47 Wattlebrook Drive, Fernhollow Vic 3091
Phone - 1800 462 817
email - enquiries@keepsteady.com.au
Internet - www.keepsteady.com.au
ABN - 82 463 915 207
ACN - 264 871 035

Files need to be able to be edited in Illustrator CS2

Business Cards / with compliments slips / email stationary:
Double sided.
One side to have Name, Mobile number, company phone 1800462817, email, internet address

Files need to be able to be edited in Illustrator CS2 (except email stationary)

Our website is www.keepsteady.com.au for more information. Do not base designs on the website as it will eventually be revised.

Target Market(s)

Australian based businesses, government departments and schools. We specialise in corporate customers rather than public first aid course

Industry/Entity Type

Internet

Requirements
Must have
• Where applicable file to be editable in illustrator CS2 to allow future alterations.

```html
<!DOCTYPE html>
<html lang="en">
<head>
<meta charset="utf-8">
<title>Keeping Steady – Stationery</title>
<link rel="stylesheet" href="https://fonts.googleapis.com/css2?family=Open+Sans:wght@400;600;700&display=swap">
<style>
  :root{
    --red:#e0121b;
    --red-deep:#a8000b;
    --red-band:#c80812;
    --ink:#1a1a1a;
    --paper:#ffffff;
  }
  *{box-sizing:border-box;margin:0;padding:0}
  html,body{width:918px;height:1200px;overflow:hidden;background:var(--paper)}
  body{position:relative;font-family:"Open Sans",Arial,sans-serif;color:var(--ink)}

  .brand{position:absolute;display:flex;align-items:center;gap:10px}
  .brand-square{background:var(--red);flex:none}
  .brand-name{color:var(--red);font-weight:700;line-height:1.1}

  /* Letterhead */
  .letterhead{position:absolute;left:54px;top:37px;width:554px;height:782px;border:1px solid #9a9a9a;border-bottom:none;background:var(--paper)}
  .letterhead .brand{left:27px;top:40px}
  .letterhead .brand-square{width:34px;height:34px}
  .letterhead .brand-name{font-size:19px;width:210px}
  .lh-footer{position:absolute;left:38px;top:712px;display:flex;font-size:8px;line-height:14px;white-space:nowrap}
  .lh-address{width:120px}
  .lh-divider{width:1px;background:#555;height:36px;margin:2px 8px 0}
  .lh-contact{width:140px;font-weight:600}
  .lh-contact li,.contact-list li{list-style:none;display:flex;align-items:center;gap:5px}
  .lh-ids{font-size:7px;line-height:14px;padding-top:7px}
  .lh-band{position:absolute;left:0;bottom:0;width:487px;height:16px;background:var(--red-band)}
  .icon{width:10px;height:10px;flex:none}

  /* Business cards */
  .card-front{position:absolute;left:540px;top:180px;width:295px;height:179px;border:1px solid #777;
    background:linear-gradient(100deg,var(--red-deep) 0%,#d10612 45%,var(--red) 100%)}
  .card-front .panel{position:absolute;left:0;top:38px;width:263px;height:88px;background:var(--paper);box-shadow:3px 4px 6px rgba(0,0,0,.35)}
  .card-front .brand{left:26px;top:24px}
  .card-front .brand-square{width:26px;height:26px}
  .card-front .brand-name{font-size:16px;width:200px}
  .card-url{position:absolute;left:32px;top:145px;color:#fff;font-size:12.5px;letter-spacing:3.2px}
  .card-url b{font-weight:700}

  .card-back{position:absolute;left:539px;top:371px;width:295px;height:179px;border:1px solid #888;background:var(--paper)}
  .card-back .brand{left:20px;top:20px}
  .card-back .brand-square{width:24px;height:24px}
  .card-back .brand-name{font-size:14px;width:170px}
  .person{position:absolute;font-size:10.5px;letter-spacing:.5px;line-height:1.2;white-space:nowrap}
  .person small{display:block;font-size:7px;letter-spacing:.6px}
  .card-back .person{left:20px;top:84px}
  .contact-list{position:absolute;font-size:7.2px;line-height:10.8px;letter-spacing:.4px;white-space:nowrap}
  .contact-list .web{color:var(--red);font-weight:700}
  .card-back .contact-list{left:149px;top:86px}
  .card-back .red-rule{position:absolute;left:0;bottom:2px;width:275px;height:3px;background:var(--red)}

  /* Compliments slip */
  .slip{position:absolute;left:230px;top:872px;width:624px;height:279px;border:1px solid #999;
    background:linear-gradient(180deg,#fff 0%,#fff 80%,#e6e6e6 100%);overflow:hidden}
  .slip .brand{left:25px;top:26px}
  .slip .brand-square{width:34px;height:34px}
  .slip .brand-name{font-size:20px;width:230px}
  .slip .person{left:467px;top:34px;font-size:11px}
  .slip .contact-list{left:467px;top:50px;font-size:7.2px;line-height:10.6px}
  .compliments{position:absolute;left:0;top:177px;width:302px;height:55px;
    background:linear-gradient(90deg,var(--red-deep),var(--red));color:#fff;font-size:29px;
    padding:10px 0 0 31px;box-shadow:4px 4px 6px rgba(0,0,0,.3);white-space:nowrap}
  .ribbon-art{position:absolute;left:574px;top:0;width:50px;height:262px;
    background:linear-gradient(200deg,rgba(200,0,10,.85) 0%,rgba(230,40,50,.35) 45%,rgba(255,255,255,0) 100%)}
</style>
</head>
<body>

<section class="letterhead" aria-label="Letterhead">
  <div class="brand"><span class="brand-square"></span><span class="brand-name">Keeping Steady Paramedical Services</span></div>
  <footer class="lh-footer">
    <p class="lh-address">Address - 47 Wattlebrook Drive,<br>Fernhollow Vic 3091<br>Australia</p>
    <span class="lh-divider"></span>
    <ul class="lh-contact">
      <li><svg class="icon" viewBox="0 0 10 10"><circle cx="5" cy="5" r="5" fill="#e0121b"/><rect x="2.5" y="3" width="5" height="4" rx="1" fill="#fff"/></svg>1800 462 817</li>
      <li><svg class="icon" viewBox="0 0 10 10"><rect x="0.5" y="2" width="9" height="6" fill="#e0121b"/><path d="M.5 2 5 5.5 9.5 2" stroke="#fff" fill="none"/></svg>enquiries@keepsteady.com.au</li>
      <li><svg class="icon" viewBox="0 0 10 10"><circle cx="5" cy="5" r="4.5" fill="#e0121b"/><path d="M.5 5h9M5 .5v9" stroke="#fff" stroke-width=".8"/></svg>www.keepsteady.com.au</li>
    </ul>
    <span class="lh-divider"></span>
    <p class="lh-ids">ABN - 82 463 915 207<br>ACN - 264 871 035</p>
  </footer>
  <div class="lh-band"></div>
</section>

<section class="card-front" aria-label="Business card front">
  <div class="panel">
    <div class="brand"><span class="brand-square"></span><span class="brand-name">Keeping Steady Paramedical Services</span></div>
  </div>
  <p class="card-url">www.<b>keepsteady</b>.com.au</p>
</section>

<section class="card-back" aria-label="Business card back">
  <div class="brand"><span class="brand-square"></span><span class="brand-name">Keeping Steady Paramedical Services</span></div>
  <p class="person">Daniel Harrow<small>Paramedical Manager</small></p>
  <ul class="contact-list">
    <li>47 Wattlebrook Drive,</li>
    <li>Fernhollow Vic 3091</li>
    <li><svg class="icon" viewBox="0 0 10 10"><rect x="1" y="3" width="8" height="5" rx="1" fill="#e0121b"/></svg>1800 462 817</li>
    <li><svg class="icon" viewBox="0 0 10 10"><rect x="2.5" y="0.5" width="5" height="9" rx="1" fill="#e0121b"/></svg>1800 462 817</li>
    <li><svg class="icon" viewBox="0 0 10 10"><rect x="0.5" y="2" width="9" height="6" fill="#e0121b"/><path d="M.5 2 5 5.5 9.5 2" stroke="#fff" fill="none"/></svg>enquiries@keepsteady.com.au</li>
    <li class="web"><svg class="icon" viewBox="0 0 10 10"><circle cx="5" cy="5" r="4.5" fill="#e0121b"/></svg>keepsteady.com.au</li>
  </ul>
  <div class="red-rule"></div>
</section>

<section class="slip" aria-label="With compliments slip">
  <div class="brand"><span class="brand-square"></span><span class="brand-name">Keeping Steady Paramedical Services</span></div>
  <div class="ribbon-art" role="img" aria-label="Flowing red ribbon illustration"></div>
  <p class="person">Daniel Harrow</p>
  <ul class="contact-list">
    <li>47 Wattlebrook Drive,</li>
    <li>Fernhollow Vic 3091</li>
    <li><svg class="icon" viewBox="0 0 10 10"><rect x="1" y="3" width="8" height="5" rx="1" fill="#e0121b"/></svg>1800 462 817</li>
    <li><svg class="icon" viewBox="0 0 10 10"><rect x="2.5" y="0.5" width="5" height="9" rx="1" fill="#e0121b"/></svg>1800 462 817</li>
    <li><svg class="icon" viewBox="0 0 10 10"><rect x="0.5" y="2" width="9" height="6" fill="#e0121b"/><path d="M.5 2 5 5.5 9.5 2" stroke="#fff" fill="none"/></svg>enquiries@keepsteady.com.au</li>
    <li class="web"><svg class="icon" viewBox="0 0 10 10"><circle cx="5" cy="5" r="4.5" fill="#e0121b"/></svg>keepsteady.com.au</li>
  </ul>
  <p class="compliments">With Compliments</p>
</section>

</body>
</html>
```